Tufted Hollow is company name.Handknit&crochet blankets&scarves. Need logo&business ...

I need a design that is eye catching, using yarn and is flowing. I'd like to see colors in aqua (Larkin Peabody paint LP9043 Aquastone) for the yarn and company name. For the text, a dark grey color (Larkin Peabody LP7622 Hamburg Gray)

Colors
87cfc7

```html
<!DOCTYPE html>
<html lang="en">
<head>
<meta charset="utf-8">
<title>Tufted Hollow – Business Card</title>
<link rel="stylesheet" href="https://fonts.googleapis.com/css2?family=Red+Hat+Display:wght@400;500&display=swap">
<style>
  :root {
    --aquastone: #87cfc7;
    --aquastone-deep: #84c4b7;
    --hamburg-gray: #5f6163;
    --card-white: #ffffff;
    --backdrop: #c8c9ad;
  }
  html, body {
    margin: 0;
    padding: 0;
    width: 1200px;
    height: 900px;
    overflow: hidden;
    background: var(--backdrop);
    font-family: "Red Hat Display", sans-serif;
  }
  .business-card {
    position: absolute;
    left: 100px;
    top: 164px;
    width: 1000px;
    height: 572px;
    background: var(--card-white);
    box-shadow: 0 10px 30px rgba(60, 62, 40, 0.25);
    overflow: hidden;
  }
  .brand {
    position: absolute;
    top: 110px;
    left: 0;
    width: 100%;
    text-align: center;
    color: var(--aquastone);
  }
  .brand-name {
    display: inline-flex;
    align-items: center;
    gap: 22px;
    font-size: 92px;
    font-weight: 500;
    line-height: 1;
    letter-spacing: 1px;
    white-space: nowrap;
  }
  .brand-dot {
    width: 58px;
    height: 58px;
    border-radius: 50%;
    background: var(--aquastone);
    flex: none;
  }
  .brand-maker {
    margin-top: 26px;
    font-size: 40px;
    font-weight: 500;
    letter-spacing: 1px;
    white-space: nowrap;
  }
  .brand-maker .by {
    font-size: 28px;
    margin-right: 6px;
  }
  .contact-band {
    position: absolute;
    left: 0;
    top: 404px;
    width: 100%;
    height: 70px;
    background: var(--aquastone-deep);
    display: flex;
    align-items: center;
    justify-content: center;
    gap: 40px;
    color: var(--card-white);
    font-size: 31px;
    font-weight: 400;
    white-space: nowrap;
  }
  .contact-item {
    display: flex;
    align-items: center;
    gap: 8px;
  }
  .contact-item svg {
    width: 28px;
    height: 28px;
    fill: none;
    stroke: var(--card-white);
    stroke-width: 2.4;
    stroke-linejoin: round;
  }
  .contact-item .phone-icon {
    fill: var(--card-white);
    stroke: none;
  }
  .services {
    position: absolute;
    left: 0;
    top: 474px;
    width: 100%;
    height: 98px;
    display: flex;
    align-items: center;
    justify-content: center;
    color: var(--hamburg-gray);
    font-size: 27px;
    font-weight: 400;
    letter-spacing: 0.2px;
    white-space: nowrap;
  }
</style>
</head>
<body>
  <div class="business-card">
    <div class="brand">
      <div class="brand-name"><span class="brand-dot"></span>Tufted Hollow</div>
      <div class="brand-maker"><span class="by">by</span>Dana Whitcombe</div>
    </div>

    <div class="contact-band">
      <span class="contact-item">
        <svg class="phone-icon" viewBox="0 0 24 24" aria-hidden="true"><path d="M6.6 10.8a15.1 15.1 0 0 0 6.6 6.6l2.2-2.2c.3-.3.7-.4 1-.2 1.1.4 2.3.6 3.6.6.6 0 1 .4 1 1V20c0 .6-.4 1-1 1A17 17 0 0 1 3 4c0-.6.4-1 1-1h3.5c.6 0 1 .4 1 1 0 1.3.2 2.5.6 3.6.1.3 0 .7-.2 1z"/></svg>
        (555) 014-2278
      </span>
      <span class="contact-item">
        <svg viewBox="0 0 24 24" aria-hidden="true"><rect x="2.5" y="5" width="19" height="14" rx="1"/><path d="M2.5 5.5 12 13l9.5-7.5M2.5 18.5l7-6.5M21.5 18.5l-7-6.5"/></svg>
        tuftedhollowbydana@mailbox.example
      </span>
    </div>

    <div class="services">Hand Knit | Crochet | Baby Afghans | Afghans | Scarves, Gloves, Hats</div>
  </div>
</body>
</html>
```